Flyer redesign

We need this flier {Seasonal Care back 2018} redesigned for our 2019 season. It is attached below. New design should look different from current design. Be creative yet still professional.

Requirements
Must have
• Designed in photoshop.
• Should have the same text as current design. Only is "2019" instead of 2018. We want a different look with same info to send our customers next year.
• size: standard letter paper 8.5" x 11"
Nice to have
• Can use optional images provided. Not required though. See our website for more photos. thornbrookmemorial.org. send message through briskdrafts if you want a specific photo.
Should not have
• Do not take current design and just change date or image. Make the design look different.

```html
<!DOCTYPE html>
<html lang="en">
<head>
<meta charset="utf-8">
<title>2019 Gravesite Landscaping Packages</title>
<link href="https://fonts.googleapis.com/css2?family=Montserrat:wght@400;500;700;800&family=Source+Sans+3:wght@400;600&display=swap" rel="stylesheet">
<style>
:root{
  --stage:#34504a;
  --maroon:#7b1c2c;
  --maroon-dark:#6c1524;
  --green-light:#cfe2b8;
  --green-mid:#b3d08f;
  --green-deep:#97bc6b;
  --frame:#d9eac6;
  --ink:#2a2a22;
  --white:#ffffff;
}
*{box-sizing:border-box;margin:0;padding:0}
html,body{width:1200px;height:1200px;overflow:hidden}
body{background:var(--stage);font-family:"Source Sans 3",sans-serif;position:relative}
.flyer{position:absolute;left:175px;top:50px;width:850px;height:1100px;background:var(--white);overflow:hidden}
.hero{position:absolute;left:0;top:0;width:850px;height:930px;
  background:linear-gradient(180deg,#6e1f24 0%,#7a4a2a 9%,#4f6a32 22%,#6f8c55 36%,#9ab386 48%,#a9c18a 58%,#8fb062 70%,#c9d9b5 86%,#ffffff 100%)}
.title{position:absolute;left:0;right:0;top:46px;text-align:center;color:var(--white);
  font-family:"Montserrat",sans-serif;font-weight:800;font-size:44px;line-height:44px;letter-spacing:-0.5px}
.package{position:absolute;top:373px;width:255px;height:553px}
.package--seasonal{left:31px}
.package--basic{left:298px}
.package--perpetual{left:565px}
.package__arc{position:absolute;left:18px;right:18px;top:0;height:70px;
  border-top:11px solid var(--maroon);border-radius:50% 50% 0 0 / 100% 100% 0 0}
.package__photo{position:absolute;left:0;right:0;top:10px;height:206px;
  border-radius:50% 50% 0 0 / 34% 34% 0 0}
.package--seasonal .package__photo{background:linear-gradient(180deg,#a9b7c5 0%,#6b3a55 30%,#5c7d3e 65%,#a8b5a6 100%)}
.package--basic .package__photo{background:linear-gradient(180deg,#8fa86a 0%,#5f8638 40%,#7ea650 70%,#95b86a 100%)}
.package--perpetual .package__photo{background:linear-gradient(180deg,#7ea6d8 0%,#a9c3e2 35%,#4d6b3a 58%,#8e9a8c 80%,#7b945c 100%)}
.package__panel{position:absolute;left:0;right:0;top:216px;bottom:0;padding:7px;background:var(--frame)}
.package__body{height:100%;padding:16px 18px 10px;background:linear-gradient(180deg,var(--green-light) 0%,var(--green-mid) 55%,var(--green-deep) 100%);
  color:var(--ink);text-align:center;display:flex;flex-direction:column}
.package__name{font-family:"Montserrat",sans-serif;font-weight:800;font-size:21px;line-height:22px;color:var(--maroon)}
.package__tagline{font-family:"Montserrat",sans-serif;font-weight:500;font-size:12.5px;line-height:14px;color:var(--maroon);margin-top:3px}
.features{list-style:none;text-align:left;margin-top:16px;font-size:10.5px;line-height:13px}
.features li{position:relative;padding-left:18px;margin-bottom:5px}
.features li::before{content:"";position:absolute;left:2px;top:4px;width:5px;height:5px;border-radius:50%;background:var(--maroon)}
.rates{margin-top:10px;font-family:"Montserrat",sans-serif;font-weight:700;font-size:14px;line-height:15px;color:var(--maroon)}
.rates p{margin-bottom:15px}
.price{font-family:"Montserrat",sans-serif;font-weight:700;font-size:15px;line-height:19px;color:var(--maroon)}
.note{font-size:10.5px;line-height:12px;margin-top:auto}
.fine{font-size:7.5px;line-height:9px;margin-top:14px}
.spacer{flex:1}
.brand{position:absolute;left:0;right:0;top:960px;display:flex;align-items:center;justify-content:center;gap:16px}
.brand__mark{width:44px;height:44px;border-radius:50%;border:2px solid var(--maroon)}
.brand__name{font-family:"Montserrat",sans-serif;font-weight:500;font-size:28px;letter-spacing:1px;color:var(--maroon)}
.contact{position:absolute;left:0;right:0;bottom:0;height:58px;background:var(--maroon-dark);color:var(--white);
  display:flex;align-items:center;justify-content:center;font-size:16px;gap:22px}
</style>
</head>
<body>
<main class="flyer">
  <div class="hero" role="img" aria-label="Photo of a cemetery lane with headstones, trimmed hedges and trees"></div>
  <h1 class="title">2019 GRAVESITE<br>LANDSCAPING PACKAGES</h1>

  <section class="package package--seasonal">
    <div class="package__photo" role="img" aria-label="Photo of a flowering purple tree among headstones"></div>
    <div class="package__arc"></div>
    <div class="package__panel"><div class="package__body">
      <h2 class="package__name">SEASONAL<br>CARE</h2>
      <p class="package__tagline">Seaonal Landscaping<br>grave care.</p>
      <ul class="features">
        <li>Weeding and trimming services on your gravesite approximately every 7 weeks during the growing season: mid-April through mid-October</li>
      </ul>
      <div class="rates">
        <p>3 Years<br>$327</p>
        <p>2 Years<br>$218</p>
        <p>1 Year<br>$109</p>
      </div>
      <p class="note">Multi-year Payment locks current rates.</p>
    </div></div>
  </section>

  <section class="package package--basic">
    <div class="package__photo" role="img" aria-label="Photo of a large shade tree over a green cemetery lawn"></div>
    <div class="package__arc"></div>
    <div class="package__panel"><div class="package__body">
      <h2 class="package__name">BASIC CARE<br>ENDOWMENT</h2>
      <p class="package__tagline">Landscaping care forever for<br>graves with no plantings.</p>
      <ul class="features">
        <li>Weeding and trimming services on your gravesites 2 times per year: mid-May and Mid-September</li>
        <li>Monument leveling</li>
        <li>Payment ensures grave care forever</li>
      </ul>
      <div class="spacer"></div>
      <p class="price">12 Monthly<br>payments<br>of $225</p>
      <p class="fine">*gravesites with single headstones. Call for other monument types and single payment discount. Valid through 10/31/18.</p>
    </div></div>
  </section>

  <section class="package package--perpetual">
    <div class="package__photo" role="img" aria-label="Photo of a wide cemetery view under a blue sky"></div>
    <div class="package__arc"></div>
    <div class="package__panel"><div class="package__body">
      <h2 class="package__name">PERPETUAL CARE<br>ENDOWMENT</h2>
      <p class="package__tagline">Landscaping care forever for<br>graves with plantings.</p>
      <ul class="features">
        <li>Weeding and trimming services on your gravesite approximately every 7 weeks during the growing season: mid-April through mid-October</li>
        <li>Monument leveling and cleaning</li>
        <li>Payment ensure grave care forever</li>
        <li>Full bed of boxwood shrubs</li>
        <li>Replacement of shrubs</li>
        <li>Trust certificate</li>
      </ul>
      <p class="price" style="margin-top:6px">12 monthly payments<br>of $280.42</p>
      <p class="note" style="margin-top:2px">Call for single payment discount<br>Valid 10/30/18.</p>
    </div></div>
  </section>

  <div class="brand">
    <span class="brand__name">THORNBROOK</span>
    <span class="brand__mark"></span>
    <span class="brand__name">MEMORIAL</span>
  </div>

  <footer class="contact">
    <span>info@thornbrookmemorial.org</span><span>|</span>
    <span>(555) 214-0386</span><span>|</span>
    <span>www.thornbrookmemorial.org</span>
  </footer>
</main>
</body>
</html>
```